Child Care Web Page

We need a web page for a child care center, children ages 6 weeks to prekindergarten. We are licensed by the state of Colorado, accredited by the Federated Council for Early Learning Standards Review. The design should be colorful, parent and user friendly.
Updates

Project Deadline Extended
Reason: Difficulty of project

Target Market(s)

Parents, staff, general community, early childhood professionals

Industry/Entity Type

Education

Requirements
Must have
• I would like to have designers that are willing to work with me in developing a site that I am able to make changes to and help with the learning curve.

```html
<!DOCTYPE html>
<html lang="en">
<head>
<meta charset="utf-8">
<title>Little Meadow School – Child Care</title>
<link rel="stylesheet" href="https://fonts.googleapis.com/css2?family=Chewy&family=Gelasio:wght@400;500&display=swap">
<style>
  :root {
    --red: #e9472a;
    --orange: #f6a400;
    --amber: #f8ad0c;
    --ink: #2b2b2b;
    --grey: #7d7d7d;
    --paper: #fbfbfb;
    --panel: #f3f2ee;
    --line: #c9c9c9;
    --sky: #8fc9e4;
    --band: #fbab00;
  }
  * { box-sizing: border-box; margin: 0; padding: 0; }
  html, body { width: 1200px; height: 675px; overflow: hidden; }
  body {
    position: relative;
    background: radial-gradient(ellipse at 40% 30%, #ffffff 0%, #f5f5f5 60%, #efefef 100%);
    font-family: "Gelasio", Georgia, serif;
    color: var(--ink);
  }
  .display { font-family: "Chewy", cursive; font-weight: 400; }

  /* header */
  .brand {
    position: absolute; left: 174px; top: 38px;
    display: flex; align-items: center; gap: 10px;
    font-family: "Chewy", cursive; font-size: 40px; color: var(--red);
    letter-spacing: 0.5px; line-height: 1;
  }
  .brand-dot { width: 22px; height: 22px; border-radius: 50%; background: var(--orange); }
  .main-nav { position: absolute; top: 56px; left: 628px; display: flex; gap: 24px; }
  .main-nav a {
    font-family: "Chewy", cursive; font-size: 15px; color: var(--orange);
    text-decoration: none; display: flex; align-items: center; gap: 2px;
  }
  .main-nav a.is-current, .main-nav a.contact { color: var(--red); }
  .main-nav a.contact { color: var(--orange); }
  .main-nav a.is-current { color: var(--red); }
  .main-nav svg { width: 9px; height: 9px; }

  /* theme swatches */
  .swatches { position: absolute; left: 16px; top: 145px; display: flex; flex-direction: column; gap: 5px; }
  .swatch { width: 21px; height: 21px; border: 2px dashed #cfcfcf; background: #fff; padding: 1px; display: flex; flex-direction: column; }
  .swatch span { flex: 1; }

  /* decorative sketches */
  .sketch { position: absolute; opacity: 0.35; border-radius: 6px; }
  .sketch-swing { left: 84px; top: 218px; width: 90px; height: 124px; background: linear-gradient(180deg, #f7b7a8, #f08a72); }
  .sketch-slide { left: 1010px; top: 286px; width: 52px; height: 54px; background: linear-gradient(180deg, #fbe1a0, #f6c24a); }

  /* hero */
  .hero-wash { position: absolute; left: 360px; top: 370px; width: 460px; height: 40px; background: radial-gradient(ellipse, rgba(246,196,80,.45), rgba(246,196,80,0) 70%); }
  .hero-wash-top { position: absolute; left: 440px; top: 92px; width: 340px; height: 40px; background: radial-gradient(ellipse, rgba(143,201,228,.35), rgba(143,201,228,0) 70%); }
  .slider {
    position: absolute; left: 174px; top: 117px; width: 574px; height: 265px;
    background: linear-gradient(180deg, #f7f6f2, #ecebe5);
    box-shadow: 0 2px 5px rgba(0,0,0,.12);
  }
  .slider-photo {
    position: absolute; left: 5px; top: 9px; width: 563px; height: 218px;
    background: linear-gradient(90deg, #b99fe0 0%, #a8de63 20%, #a43ac0 38%, #b7102a 55%, #d6b34a 72%, #f07a1c 88%, #49c7d6 100%);
  }
  .pager { position: absolute; right: 10px; bottom: 12px; display: flex; gap: 5px; font-family: "Chewy", cursive; font-size: 12px; color: var(--orange); align-items: center; }
  .pager .is-active { color: var(--red); }
  .pager .sep { color: #bbb; }

  .program { position: absolute; left: 748px; top: 117px; width: 262px; height: 265px; background: rgba(255,255,255,.7); }
  .program h2 { position: absolute; left: 22px; top: 22px; font-family: "Chewy", cursive; font-weight: 400; font-size: 25px; color: var(--red); }
  .program .rule { position: absolute; left: 22px; top: 58px; width: 155px; border-top: 2px dotted var(--line); }
  .program ul { list-style: none; position: absolute; left: 22px; top: 77px; }
  .program li { height: 57px; }
  .program li h3 { font-weight: 400; font-size: 20px; color: var(--orange); line-height: 1.05; }
  .program li p { font-size: 8px; color: #555; }
  .program-scroll { position: absolute; right: 0; top: 0; width: 52px; height: 262px; border: 1.5px solid #f8c95a; border-radius: 3px; }
  .program-scroll svg { position: absolute; left: 10px; width: 30px; height: 30px; }
  .program-scroll .up { top: 12px; }
  .program-scroll .down { bottom: 10px; }
  .program-scroll .tick { position: absolute; left: 8px; width: 36px; border-top: 1px solid #f8c95a; }

  /* about */
  .about { position: absolute; left: 174px; top: 417px; width: 540px; }
  .section-title { font-family: "Chewy", cursive; font-weight: 400; font-size: 24px; color: var(--red); line-height: 1; }
  .about p { margin-top: 15px; font-size: 12.3px; line-height: 20px; color: var(--ink); }
  .read-more { margin-top: 10px; display: flex; align-items: center; gap: 8px; font-family: "Chewy", cursive; font-size: 19px; color: var(--red); text-decoration: none; }
  .read-more svg { width: 32px; height: 32px; }

  .hours { position: absolute; left: 749px; top: 417px; width: 262px; }
  .hours .section-title { color: var(--orange); }
  .hours-row { display: flex; gap: 20px; margin-top: 13px; }
  .hours-row svg { width: 38px; height: 38px; flex: none; }
  .hours-row small { display: block; font-size: 8.5px; color: var(--grey); text-transform: uppercase; }
  .hours-row strong { display: block; font-weight: 400; font-size: 17px; margin-top: 2px; }
  .hours .rule { margin: 10px 0 0 58px; border-top: 2px dotted var(--line); }

  /* bottom band */
  .features { position: absolute; left: 0; top: 584px; width: 1200px; height: 91px; background: var(--band); }
  .features .zigzag { position: absolute; left: 0; top: -9px; width: 1200px; height: 10px; }
  .feature { position: absolute; top: 34px; }
  .feature h3 { font-weight: 400; font-size: 20px; color: #fff; }
  .feature p { font-size: 9.5px; font-weight: 500; color: var(--red); text-transform: uppercase; margin-top: 5px; }
</style>
</head>
<body>

<header>
  <div class="brand"><span class="brand-dot"></span>Little Meadow School</div>
  <nav class="main-nav">
    <a href="#" class="is-current">HOME</a>
    <a href="#">ABOUT</a>
    <a href="#">SAMPLE<svg viewBox="0 0 10 10"><path d="M1 2l4 3 4-3M1 6l4 3 4-3" fill="none" stroke="currentColor" stroke-width="1.4"/></svg></a>
    <a href="#">BLOG<svg viewBox="0 0 10 10"><path d="M1 2l4 3 4-3M1 6l4 3 4-3" fill="none" stroke="currentColor" stroke-width="1.4"/></svg></a>
    <a href="#">GALLERY<svg viewBox="0 0 10 10"><path d="M1 2l4 3 4-3M1 6l4 3 4-3" fill="none" stroke="currentColor" stroke-width="1.4"/></svg></a>
    <a href="#" class="contact">CONTACT</a>
  </nav>
</header>

<div class="swatches" aria-label="Colour themes">
  <div class="swatch"><span style="background:#c8d22a"></span><span style="background:#2a7bc8"></span></div>
  <div class="swatch"><span style="background:#2a2a38"></span><span style="background:#c8203a"></span></div>
  <div class="swatch"><span style="background:#e8601c"></span><span style="background:#c81e1e"></span></div>
  <div class="swatch"><span style="background:#f0608a"></span><span style="background:#555b66"></span></div>
  <div class="swatch"><span style="background:#c8a86a"></span><span style="background:#c8203a"></span></div>
  <div class="swatch"><span style="background:#2aa0b0"></span><span style="background:#222"></span></div>
  <div class="swatch"><span style="background:#8aa89a"></span><span style="background:#9a9a9a"></span></div>
  <div class="swatch"><span style="background:#5ac8d8"></span><span style="background:#e0302a"></span></div>
  <div class="swatch"><span style="background:#f8b000"></span><span style="background:#e83a1a"></span></div>
  <div class="swatch"><span style="background:#8a6ac0"></span><span style="background:#f8c800"></span></div>
</div>

<div class="sketch sketch-swing" role="img" aria-label="Hand-drawn sketch of a playground swing"></div>
<div class="sketch sketch-slide" role="img" aria-label="Hand-drawn sketch of a playground slide"></div>

<section class="hero">
  <div class="hero-wash-top"></div>
  <div class="hero-wash"></div>
  <div class="slider">
    <div class="slider-photo" role="img" aria-label="Photo of smiling children in colourful clothes lying side by side on a blue floor"></div>
    <div class="pager"><span>&laquo;</span><span class="sep">|</span><span class="is-active">2</span><span>3</span><span>4</span><span>5</span><span>&raquo;</span></div>
  </div>
  <aside class="program">
    <h2>OUR PROGRAM</h2>
    <div class="rule"></div>
    <ul>
      <li><h3>Infant</h3><p>Lorem ipsum dolor sit amet sit amet</p></li>
      <li><h3>Pre-toddlers</h3><p>Lorem ipsum dolor sit amet</p></li>
      <li><h3>Toddlers</h3><p>Lorem ipsum dolor sit amet</p></li>
    </ul>
    <div class="program-scroll">
      <svg class="up" viewBox="0 0 30 30"><circle cx="15" cy="15" r="13" fill="none" stroke="#f6a400" stroke-width="2"/><path d="M9 16l6-6 6 6M9 21l6-6 6 6" fill="none" stroke="#f6a400" stroke-width="2"/></svg>
      <div class="tick" style="top:49px"></div>
      <div class="tick" style="top:212px"></div>
      <svg class="down" viewBox="0 0 30 30"><circle cx="15" cy="15" r="13" fill="none" stroke="#f6a400" stroke-width="2"/><path d="M9 9l6 6 6-6M9 14l6 6 6-6" fill="none" stroke="#f6a400" stroke-width="2"/></svg>
    </div>
  </aside>
</section>

<section class="about">
  <h2 class="section-title">ABOUT THE SCHOOL</h2>
  <p>Nemo enim ipsam voluptatem quia voluptas sit aspernatur aut odit aut fugit. tempora incidunt ut labore et dolore magnam aliquam quaerat voluptatem. Ut enim ad minima veniam, quis nostrum exercitationem ullam corporis suscipit laboriosam, nisi ut aliquid ex ea commodi consequatur?</p>
  <a href="#" class="read-more">READ MORE
    <svg viewBox="0 0 32 32"><circle cx="16" cy="16" r="14" fill="none" stroke="#e9472a" stroke-width="2"/><path d="M11 12l4 4-4 4M16 12l4 4-4 4" fill="none" stroke="#e9472a" stroke-width="2"/></svg>
  </a>
</section>

<section class="hours">
  <h2 class="section-title">WORKING HOURS</h2>
  <div class="hours-row">
    <svg viewBox="0 0 38 38"><circle cx="19" cy="19" r="17" fill="none" stroke="#f6a400" stroke-width="2"/><path d="M19 8v11l7 6" fill="none" stroke="#f6a400" stroke-width="2" stroke-linecap="round"/></svg>
    <div><small>7 days a week</small><strong>10:00 am - 1:30 pm</strong></div>
  </div>
  <div class="rule"></div>
  <div class="hours-row">
    <svg viewBox="0 0 38 38"><path d="M4 14c0-6 30-6 30 0v3h-7v-3H11v3H4z" fill="none" stroke="#f6a400" stroke-width="2"/><rect x="8" y="18" width="22" height="16" rx="3" fill="none" stroke="#f6a400" stroke-width="2"/><circle cx="19" cy="26" r="4" fill="none" stroke="#f6a400" stroke-width="2"/></svg>
    <div><small>Contact phone</small><strong>+321 0555 010 2200</strong></div>
  </div>
</section>

<section class="features">
  <svg class="zigzag" viewBox="0 0 1200 10" preserveAspectRatio="none"><path d="M0 10 L0 5 L6 0 L12 5 L18 0 L24 5 L30 0 L36 5 L42 0 L48 5 L54 0 L60 5 L66 0 L72 5 L78 0 L84 5 L90 0 L96 5 L102 0 L108 5 L114 0 L120 5 L126 0 L132 5 L138 0 L144 5 L150 0 L156 5 L162 0 L168 5 L174 0 L180 5 L186 0 L192 5 L198 0 L204 5 L210 0 L216 5 L222 0 L228 5 L234 0 L240 5 L246 0 L252 5 L258 0 L264 5 L270 0 L276 5 L282 0 L288 5 L294 0 L300 5 L306 0 L312 5 L318 0 L324 5 L330 0 L336 5 L342 0 L348 5 L354 0 L360 5 L366 0 L372 5 L378 0 L384 5 L390 0 L396 5 L402 0 L408 5 L414 0 L420 5 L426 0 L432 5 L438 0 L444 5 L450 0 L456 5 L462 0 L468 5 L474 0 L480 5 L486 0 L492 5 L498 0 L504 5 L510 0 L516 5 L522 0 L528 5 L534 0 L540 5 L546 0 L552 5 L558 0 L564 5 L570 0 L576 5 L582 0 L588 5 L594 0 L600 5 L606 0 L612 5 L618 0 L624 5 L630 0 L636 5 L642 0 L648 5 L654 0 L660 5 L666 0 L672 5 L678 0 L684 5 L690 0 L696 5 L702 0 L708 5 L714 0 L720 5 L726 0 L732 5 L738 0 L744 5 L750 0 L756 5 L762 0 L768 5 L774 0 L780 5 L786 0 L792 5 L798 0 L804 5 L810 0 L816 5 L822 0 L828 5 L834 0 L840 5 L846 0 L852 5 L858 0 L864 5 L870 0 L876 5 L882 0 L888 5 L894 0 L900 5 L906 0 L912 5 L918 0 L924 5 L930 0 L936 5 L942 0 L948 5 L954 0 L960 5 L966 0 L972 5 L978 0 L984 5 L990 0 L996 5 L1002 0 L1008 5 L1014 0 L1020 5 L1026 0 L1032 5 L1038 0 L1044 5 L1050 0 L1056 5 L1062 0 L1068 5 L1074 0 L1080 5 L1086 0 L1092 5 L1098 0 L1104 5 L1110 0 L1116 5 L1122 0 L1128 5 L1134 0 L1140 5 L1146 0 L1152 5 L1158 0 L1164 5 L1170 0 L1176 5 L1182 0 L1188 5 L1194 0 L1200 5 L1200 10 Z" fill="#fbab00"/></svg>
  <div class="feature" style="left:174px"><h3>What we do</h3><p>Lorem ipsum dolor sit amet</p></div>
  <div class="feature" style="left:462px"><h3>School approach</h3><p>Lorem ipsum dolor sit amet</p></div>
  <div class="feature" style="left:749px"><h3>Active learning</h3><p>Lorem ipsum dolor sit amet</p></div>
</section>

</body>
</html>
```